Wander Glade Journeys Stationary
Business card, envelopes and letterhead layout
Please add business cards for these people to design 106 in the same format. They do not mailing address information or separate cell phone.
Nora Pell Travel Consultant
nora.pell@wanderglade.example
Glen Ashby Marketing Director
glen.ashby@wanderglade.example
Tessa Vandrunen Travel Consultant
tessa.vandrunen@wanderglade.example
Megan Tully Travel Consultant
megan.tully@wanderglade.example
Jodi Farley Travel Consultant
jodi.farley@wanderglade.example
For the phone and cell numbers, please have the phone number have punctuation. When I submitted the brief it made me take it out. Should be 555.204.7719 and 555.316.8245
I am liking the designs. I don't want to incorporate the darker red color into the design. I like the shadowed look of the logo in the designs by vespiq. Is that meant to be on the back?
I would like to have designs for letterhead, envelopes, business cards and email signature.
I have decided I would like to have 2 sided business cards. On the back,
Where can we take you?
Honeymoons
Destination Weddings
Family Travel
Celebration Vacations

```html
<!DOCTYPE html>
<html lang="en">
<head>
<meta charset="utf-8">
<title>Wander Glade Journeys Stationery</title>
<link rel="stylesheet" href="https://fonts.googleapis.com/css2?family=Open+Sans:wght@400;600;700&display=swap">
<style>
:root{
  --bg:#ece9e4;
  --paper:#ffffff;
  --ink:#4a4a4a;
  --ink-soft:#8a8a8a;
  --rule:#dddddd;
  --red:#e8392b;
  --orange:#f7941d;
  --yellow:#fcc30b;
  --shade:rgba(0,0,0,.18);
  --band:linear-gradient(90deg,var(--yellow),var(--orange) 45%,var(--red));
}
*{margin:0;padding:0;box-sizing:border-box}
html,body{width:1200px;height:730px;overflow:hidden}
body{background:var(--bg);font-family:"Open Sans",Arial,sans-serif;color:var(--ink);position:relative}
.sheet{position:absolute;background:var(--paper);box-shadow:0 6px 16px var(--shade);overflow:hidden}
.brand{display:flex;align-items:center;gap:6px}
.brand-dot{border-radius:50%;background:var(--red);flex:none}
.brand-name{font-weight:700;color:var(--red);line-height:1.1}
.tagline{font-size:6px;letter-spacing:1.5px;color:var(--ink-soft);text-transform:uppercase}
.band{position:absolute;left:0;right:0;bottom:0;background:var(--band);color:#fff;font-size:8px;letter-spacing:1px;display:flex;align-items:center;justify-content:flex-end;padding-right:12px}
.watermark{position:absolute;border-radius:50%;background:radial-gradient(circle,rgba(232,57,43,.12),rgba(247,148,29,.05) 70%,transparent 72%)}
.palms{position:absolute;background:linear-gradient(180deg,rgba(120,160,90,.18),rgba(120,160,90,.04))}
.detail{font-size:7px;line-height:1.5;color:var(--ink)}
.detail strong{color:var(--red);font-weight:700}
.name{font-weight:700;color:var(--red);line-height:1.2}
.role{color:var(--ink-soft)}

/* letterhead */
.letterhead{left:430px;top:30px;width:300px;height:390px}
.letterhead .brand{position:absolute;top:28px;left:0;right:0;flex-direction:column;text-align:center;gap:4px}
.letterhead .brand-dot{width:20px;height:20px}
.letterhead .brand-name{font-size:13px}
.letterhead .contact{position:absolute;top:88px;left:0;right:0;text-align:center;font-size:6px;color:var(--ink-soft)}
.letterhead .watermark{width:220px;height:220px;left:40px;top:140px}
.letterhead .band{height:14px}

/* envelope */
.envelope{left:770px;top:30px;width:390px;height:180px}
.envelope .brand{position:absolute;top:22px;left:22px}
.envelope .brand-dot{width:16px;height:16px}
.envelope .brand-name{font-size:11px}
.envelope .detail{position:absolute;top:48px;left:22px;font-size:6.5px;color:var(--ink-soft)}
.envelope .watermark{width:150px;height:150px;left:220px;top:18px}
.envelope .band{height:12px;font-size:7px}

/* main business card */
.card{width:340px;height:194px}
.card-front{left:40px;top:30px}
.card-front .brand{position:absolute;top:62px;left:20px;flex-direction:column;align-items:flex-start;gap:4px}
.card-front .brand-dot{width:18px;height:18px}
.card-front .brand-name{font-size:14px;width:150px}
.card-front .divider{position:absolute;left:178px;top:24px;bottom:40px;width:1px;background:var(--rule)}
.card-front .person{position:absolute;left:192px;top:24px}
.card-front .name{font-size:10px}
.card-front .role{font-size:6.5px;margin-bottom:8px}
.card-front .detail + .detail{margin-top:8px}
.card-front .watermark{width:130px;height:130px;left:-20px;top:40px}
.card-front .band{height:18px}

.card-back{left:40px;top:246px}
.card-back .heading{position:absolute;top:24px;right:22px;font-size:12px;font-weight:700;color:var(--ink)}
.card-back ul{position:absolute;top:50px;right:22px;list-style:none}
.card-back li{font-size:8.5px;line-height:1.85;display:flex;align-items:center;justify-content:flex-end;gap:6px}
.card-back li::after{content:"";width:7px;height:7px;border-radius:50%;background:var(--orange)}
.card-back .watermark{width:200px;height:200px;left:-20px;top:10px}
.card-back .palms{left:60px;top:80px;width:110px;height:96px;border-radius:50% 50% 0 0}
.card-back .band{height:18px}

/* email signature */
.signature{left:770px;top:240px;width:390px;height:150px}
.signature .brand{position:absolute;top:30px;left:18px;flex-direction:column;align-items:flex-start;gap:4px}
.signature .brand-dot{width:16px;height:16px}
.signature .brand-name{font-size:13px;width:130px}
.signature .divider{position:absolute;top:22px;bottom:34px;width:1px;background:var(--rule)}
.signature .divider-a{left:160px}
.signature .divider-b{left:266px}
.signature .person{position:absolute;left:172px;top:30px}
.signature .name{font-size:10px}
.signature .role{font-size:6px}
.signature .detail{position:absolute;left:276px;top:26px;font-size:6.5px}
.signature .band{height:16px}

/* staff business cards */
.staff-row{position:absolute;left:40px;top:470px;width:1120px;display:flex;gap:16px}
.card-mini{position:relative;width:211px;height:120px}
.card-mini .brand{position:absolute;top:14px;left:14px;gap:5px}
.card-mini .brand-dot{width:11px;height:11px}
.card-mini .brand-name{font-size:9px}
.card-mini .rule{position:absolute;left:14px;right:14px;top:36px;height:1px;background:var(--rule)}
.card-mini .person{position:absolute;left:14px;top:44px}
.card-mini .name{font-size:9px}
.card-mini .role{font-size:6px;margin-bottom:5px}
.card-mini .detail{font-size:6px;line-height:1.45}
.card-mini .watermark{width:90px;height:90px;right:-20px;top:20px}
.card-mini .band{height:12px;font-size:6px;padding-right:10px}
</style>
</head>
<body>

<section class="sheet letterhead" aria-label="Letterhead">
  <div class="watermark"></div>
  <div class="brand">
    <span class="brand-dot"></span>
    <span class="brand-name">Wander Glade Journeys</span>
    <span class="tagline">Travel · Planned · Well</span>
  </div>
  <p class="contact">418 Fernway Rd · Brookfield, ST 00000 · 555.204.7719</p>
  <div class="band">wanderglade.example</div>
</section>

<section class="sheet envelope" aria-label="Envelope">
  <div class="watermark"></div>
  <div class="brand">
    <span class="brand-dot"></span>
    <span class="brand-name">Wander Glade Journeys</span>
  </div>
  <p class="detail">418 Fernway Rd<br>Brookfield, ST 00000</p>
  <div class="band">wanderglade.example</div>
</section>

<section class="sheet card card-front" aria-label="Business card front">
  <div class="watermark"></div>
  <div class="brand">
    <span class="brand-dot"></span>
    <span class="brand-name">Wander Glade Journeys</span>
    <span class="tagline">Travel · Planned · Well</span>
  </div>
  <div class="divider"></div>
  <div class="person">
    <p class="name">Lena Marsh</p>
    <p class="role">Owner / Travel Consultant</p>
    <p class="detail">418 Fernway Rd<br>Brookfield, ST 00000</p>
    <p class="detail"><strong>P</strong> 555.204.7719<br><strong>C</strong> 555.316.8245<br>lena.marsh@wanderglade.example<br>wanderglade.example/social</p>
  </div>
  <div class="band">wanderglade.example</div>
</section>

<section class="sheet card card-back" aria-label="Business card back">
  <div class="watermark"></div>
  <div class="palms" role="img" aria-label="Soft palm tree illustration area"></div>
  <p class="heading">Where can we take you?</p>
  <ul>
    <li>Honeymoons</li>
    <li>Destination Weddings</li>
    <li>Family Travel</li>
    <li>Celebration Vacations</li>
  </ul>
  <div class="band">wanderglade.example</div>
</section>

<section class="sheet signature" aria-label="Email signature">
  <div class="brand">
    <span class="brand-dot"></span>
    <span class="brand-name">Wander Glade Journeys</span>
    <span class="tagline">Travel · Planned · Well</span>
  </div>
  <div class="divider divider-a"></div>
  <div class="person">
    <p class="name">Lena Marsh</p>
    <p class="role">Owner / Travel Consultant</p>
  </div>
  <div class="divider divider-b"></div>
  <p class="detail">418 Fernway Rd<br>Brookfield, ST 00000<br><br><strong>P</strong> 555.204.7719<br><strong>C</strong> 555.316.8245<br>wanderglade.example/social</p>
  <div class="band">wanderglade.example</div>
</section>

<div class="staff-row">
  <section class="sheet card-mini" style="position:relative" aria-label="Business card Nora Pell">
    <div class="watermark"></div>
    <div class="brand"><span class="brand-dot"></span><span class="brand-name">Wander Glade Journeys</span></div>
    <div class="rule"></div>
    <div class="person">
      <p class="name">Nora Pell</p>
      <p class="role">Travel Consultant</p>
      <p class="detail"><strong>P</strong> 555.204.7719<br>nora.pell@wanderglade.example</p>
    </div>
    <div class="band">wanderglade.example</div>
  </section>
  <section class="sheet card-mini" style="position:relative" aria-label="Business card Glen Ashby">
    <div class="watermark"></div>
    <div class="brand"><span class="brand-dot"></span><span class="brand-name">Wander Glade Journeys</span></div>
    <div class="rule"></div>
    <div class="person">
      <p class="name">Glen Ashby</p>
      <p class="role">Marketing Director</p>
      <p class="detail"><strong>P</strong> 555.204.7719<br>glen.ashby@wanderglade.example</p>
    </div>
    <div class="band">wanderglade.example</div>
  </section>
  <section class="sheet card-mini" style="position:relative" aria-label="Business card Tessa Vandrunen">
    <div class="watermark"></div>
    <div class="brand"><span class="brand-dot"></span><span class="brand-name">Wander Glade Journeys</span></div>
    <div class="rule"></div>
    <div class="person">
      <p class="name">Tessa Vandrunen</p>
      <p class="role">Travel Consultant</p>
      <p class="detail"><strong>P</strong> 555.204.7719<br>tessa.vandrunen@wanderglade.example</p>
    </div>
    <div class="band">wanderglade.example</div>
  </section>
  <section class="sheet card-mini" style="position:relative" aria-label="Business card Megan Tully">
    <div class="watermark"></div>
    <div class="brand"><span class="brand-dot"></span><span class="brand-name">Wander Glade Journeys</span></div>
    <div class="rule"></div>
    <div class="person">
      <p class="name">Megan Tully</p>
      <p class="role">Travel Consultant</p>
      <p class="detail"><strong>P</strong> 555.204.7719<br>megan.tully@wanderglade.example</p>
    </div>
    <div class="band">wanderglade.example</div>
  </section>
  <section class="sheet card-mini" style="position:relative" aria-label="Business card Jodi Farley">
    <div class="watermark"></div>
    <div class="brand"><span class="brand-dot"></span><span class="brand-name">Wander Glade Journeys</span></div>
    <div class="rule"></div>
    <div class="person">
      <p class="name">Jodi Farley</p>
      <p class="role">Travel Consultant</p>
      <p class="detail"><strong>P</strong> 555.204.7719<br>jodi.farley@wanderglade.example</p>
    </div>
    <div class="band">wanderglade.example</div>
  </section>
</div>

</body>
</html>
```